I am looking for a stand-out cover that sings out to new parents. The category is very pastel with limited compelling covers that would make me want to buy a book. This book will be used often in the first 12 months of baby's life - so must be strong enough to sit on the bedside table or on the coffee table to inspire reading. It will be a popular gift - so needs to look credible, "pick-up-able" and loveable.

The Book Title is - The Cradle Compass to Infancy's Opening Seasons: Grounded, Research-Led Methods on Rest, Nourishment, Protection plus Growing Assurance
The Size is - 8.5 x 11 in
Book description to be provided to final design for inclusion
Some examples of book covers in this category attached. Thanks

```html
<!DOCTYPE html>
<html lang="en">
<head>
<meta charset="utf-8">
<title>The Cradle Compass to Infancy's Opening Seasons</title>
<link href="https://fonts.googleapis.com/css2?family=Arvo:wght@700&family=Allura&family=Itim&display=swap" rel="stylesheet">
<style>
  :root {
    --teal-dark: #2e6b62;
    --panel-green: #568c7a;
    --rust: #d2643a;
    --peach: #f2c7b2;
    --slate: #647d8a;
    --clay: #a57a62;
    --navy: #0b1a42;
    --white: #ffffff;
    --pill-fill: #2d6a62;
    --pill-gold: #c9952e;
    --warm-skin: #e2a47f;
    --warm-brown: #8a5a3c;
    --cream: #efdcc0;
  }
  * { margin: 0; padding: 0; box-sizing: border-box; }
  html, body { width: 928px; height: 1200px; overflow: hidden; background: #ffffff; }
  .cover {
    position: relative;
    width: 928px;
    height: 1200px;
    overflow: hidden;
    background: var(--panel-green);
    border: 1px solid #1a1a1a;
  }
  .frame-strip { position: absolute; }
  .panel {
    position: absolute;
    left: 27px; top: 26px;
    width: 872px; height: 1150px;
    background: var(--panel-green);
    overflow: hidden;
  }
  .title { position: absolute; left: 0; top: 0; width: 100%; height: 500px; }
  .title-line {
    position: absolute;
    font-family: "Arvo", "Rockwell", serif;
    font-weight: 700;
    line-height: 1;
    white-space: nowrap;
    letter-spacing: -1px;
  }
  .title-line--light { color: var(--white); font-size: 98px; }
  .title-line--dark { color: var(--navy); font-size: 66px; }
  .title-connector {
    position: absolute;
    left: 126px; top: 336px;
    font-family: "Allura", cursive;
    font-size: 104px;
    line-height: 1;
    color: var(--navy);
  }
  .subtitle-pill { position: absolute; left: 228px; top: 512px; width: 464px; height: 104px; }
  .subtitle-pill svg { position: absolute; inset: 0; }
  .subtitle-text {
    position: absolute; inset: 0;
    display: flex; align-items: center; justify-content: center;
    text-align: center;
    font-family: "Itim", cursive;
    font-size: 17px;
    line-height: 1.4;
    color: var(--white);
    padding: 0 30px;
  }
  .family-art {
    position: absolute;
    left: 0; top: 650px;
    width: 872px; height: 500px;
    background: linear-gradient(180deg, var(--panel-green) 0%, var(--warm-brown) 30%, var(--warm-skin) 65%, var(--cream) 100%);
  }
</style>
</head>
<body>
<div class="cover">
  <div class="frame-strip" style="left:0;top:0;width:210px;height:26px;background:var(--teal-dark)"></div>
  <div class="frame-strip" style="left:210px;top:0;width:255px;height:26px;background:var(--rust)"></div>
  <div class="frame-strip" style="left:465px;top:0;width:255px;height:26px;background:var(--peach)"></div>
  <div class="frame-strip" style="left:720px;top:0;width:208px;height:26px;background:var(--slate)"></div>
  <div class="frame-strip" style="left:0;top:0;width:27px;height:297px;background:var(--teal-dark)"></div>
  <div class="frame-strip" style="left:0;top:297px;width:27px;height:607px;background:var(--clay)"></div>
  <div class="frame-strip" style="left:0;top:904px;width:27px;height:296px;background:var(--teal-dark)"></div>
  <div class="frame-strip" style="left:899px;top:0;width:29px;height:293px;background:var(--slate)"></div>
  <div class="frame-strip" style="left:899px;top:293px;width:29px;height:309px;background:var(--rust)"></div>
  <div class="frame-strip" style="left:899px;top:602px;width:29px;height:299px;background:var(--peach)"></div>
  <div class="frame-strip" style="left:899px;top:901px;width:29px;height:299px;background:var(--slate)"></div>
  <div class="frame-strip" style="left:0;top:1176px;width:209px;height:24px;background:var(--teal-dark)"></div>
  <div class="frame-strip" style="left:209px;top:1176px;width:254px;height:24px;background:var(--rust)"></div>
  <div class="frame-strip" style="left:463px;top:1176px;width:255px;height:24px;background:var(--peach)"></div>
  <div class="frame-strip" style="left:718px;top:1176px;width:210px;height:24px;background:var(--slate)"></div>

  <main class="panel">
    <h1 class="title">
      <span class="title-line title-line--light" style="left:189px;top:80px">The</span>
      <span class="title-line title-line--light" style="left:138px;top:152px">Cradle</span>
      <span class="title-line title-line--light" style="left:138px;top:224px">Compass</span>
      <span class="title-connector">to</span>
      <span class="title-line title-line--dark" style="left:245px;top:318px">Infancy’s</span>
      <span class="title-line title-line--dark" style="left:245px;top:398px">Opening Seasons</span>
    </h1>

    <div class="subtitle-pill">
      <svg viewBox="0 0 464 104" width="464" height="104" aria-hidden="true">
        <path d="M30 10 C120 4 200 22 250 20 C320 16 360 6 420 8 C460 12 464 40 452 64 C442 90 418 96 378 96 C300 94 180 98 90 96 C40 96 8 100 6 80 C4 58 6 28 30 10 Z"
              fill="var(--pill-fill)" stroke="var(--pill-gold)" stroke-width="4"/>
      </svg>
      <p class="subtitle-text">Grounded, Research-Led Methods On Rest, Nourishment, Protection Plus Growing Assurance</p>
    </div>

    <div class="family-art" role="img" aria-label="Illustration of two parents leaning their heads together over a swaddled newborn"></div>
  </main>
</div>
</body>
</html>
```